Web design for Marketplace

Guys!
1st of all, thank you for willing to help me out.
I have attached PDF file with examples.
I am looking for professional and clean design for my new project “ Lantern of Seers “. Its marketplace for Psychic Readers around the world. Where they will able to register to provide their services via Chat,Email and sell their products on their personal stores.
Customer will able to get services and buy products from Psychic on Marketplace.
url : http://www.lanternofseers-demo.net
Please note: it doesn’t matter, what my current site looks like. I am looking for completely new design.
It doesn't matter if you add or remove : Vidlume video or even text which is on the home page in new design.
Following are the main pages of the website, which i am looking to be design.
1. Home page
2. Psychic
3. Marketplace
4. Psychic profile page
5. Psychic Store page
6. Psychic product page
7. Logo
following is the website, which i like the most. I would love to have something like that. It is neat , clean and friendly. I am looking for depth in design and neatness and borders (matter and a lot and it should be prefect ).
http://www.craftnook-demo.net
P.S : i believe it will be helpful to choose one of you. If you can only create design of " Homepage" at 1st , so i can go ahead and hire one of you guys.
Best,
Hi guys!
Guys,

```html
<!DOCTYPE html>
<html lang="en">
<head>
<meta charset="utf-8">
<title>Lantern of Seers — Home</title>
<link href="https://fonts.googleapis.com/css2?family=Arimo:wght@400;700&family=Gelasio:wght@700&family=Open+Sans:wght@300&display=swap" rel="stylesheet">
<style>
:root{
  --orange:#ec5a12;
  --orange-light:#f58a2a;
  --text:#1d1d1d;
  --band:#efefed;
  --card:#ebebeb;
  --card-border:#d9d9d9;
  --rule:#c9c9c9;
  --nav-top:#eeeeec;
  --nav-bottom:#cfcfcb;
  --avatar:#9a9a9a;
}
*{box-sizing:border-box;margin:0;padding:0}
html,body{width:966px;height:1200px;overflow:hidden;background:#fff}
body{position:relative;font-family:Arimo,Arial,sans-serif;color:var(--text);font-size:10px}
.abs{position:absolute}
.brand{left:95px;top:24px;width:220px}
.brand-name{font-weight:700;font-size:20px;color:#1d1d1d;line-height:1.1;display:flex;align-items:center;gap:6px;white-space:nowrap}
.brand-name i{display:inline-block;width:11px;height:11px;background:var(--orange);border-radius:50%}
.brand-tag{font-size:14px;color:#1d1d1d;margin-top:6px;white-space:nowrap}
.util{right:93px;top:44px;font-size:10px;color:#222}
.util span{margin:0 7px;color:#555}
.nav{left:84px;top:91px;width:791px;height:38px;border-radius:4px;background:linear-gradient(var(--nav-top),var(--nav-bottom));display:flex;box-shadow:0 1px 1px rgba(0,0,0,.15)}
.nav a{font-size:11px;color:#222;text-decoration:none;display:flex;align-items:center;padding-left:16px;border-right:1px solid #fff;box-shadow:1px 0 0 #bdbdb8;white-space:nowrap}
.nav a:last-child{border:none;box-shadow:none}
.hero{left:0;top:144px;width:966px;height:198px;background:var(--band);border-top:1px solid #ddd;border-bottom:1px solid #ddd}
.faces{left:91px;top:152px;display:grid;grid-template-columns:repeat(6,80px);grid-template-rows:repeat(2,83px);gap:6px}
.face{border:3px solid #fff;box-shadow:0 0 0 1px #ddd;background:linear-gradient(#a89a88,#6e5d4f)}
.pill{left:142px;top:216px;width:406px;height:53px;border-radius:14px;background:linear-gradient(var(--orange-light),var(--orange));box-shadow:0 2px 4px rgba(0,0,0,.3);color:#fff;font-family:"Open Sans",Arial,sans-serif;font-weight:300;font-size:26px;display:flex;align-items:center;justify-content:center;white-space:nowrap}
h2{font-family:Gelasio,Georgia,serif;font-weight:700;color:var(--orange);font-size:17px;white-space:nowrap}
.best{left:611px;top:156px}
.best-text{left:614px;top:184px;width:264px;font-size:9.3px;line-height:16.5px;text-align:justify}
.best-text p+p{margin-top:16px}
.top-title{left:92px;top:370px}
.card{top:406px;width:134px;height:205px;background:var(--card);border:1px solid var(--card-border)}
.card.plain{background:#fff}
.photo{position:absolute;left:9px;top:8px;width:114px;height:114px;border:1px solid #ccc}
.photo.pic{background:linear-gradient(#8a6a55,#3d2c25)}
.photo.pic2{background:linear-gradient(#6f9a4e,#2e4d2a)}
.photo.avatar{background:var(--avatar);overflow:hidden}
.nametag{position:absolute;left:0;bottom:0;width:100%;height:19px;background:rgba(60,60,60,.75);color:#fff;font-size:10.5px;display:flex;align-items:center;padding-left:6px;gap:5px}
.dot{width:7px;height:7px;border-radius:50%;background:#ddd}
.dot.on{background:#6cc63a}
.stars{position:absolute;left:10px;top:131px;display:flex;gap:1px}
.stars b{width:12px;height:12px;background:var(--orange);display:flex;align-items:center;justify-content:center}
.stars b.off{background:#ddd}
.rate{position:absolute;left:10px;display:flex;align-items:center;gap:7px;font-size:9.5px;font-weight:700;color:#333}
.r1{top:152px}.r2{top:177px}
.viewmore{right:113px;top:627px;color:var(--orange);font-size:9.5px;font-weight:700;text-decoration:underline}
.rule{left:92px;height:1px;background:var(--rule)}
.about{left:92px;top:672px}
.about-text{left:92px;top:700px;width:524px;font-size:9.8px;line-height:15px;text-align:justify}
.about-text p+p{margin-top:15px}
.video{left:625px;top:683px;width:261px;height:172px;background:#ddd;padding:4px}
.video-inner{width:100%;height:100%;background:linear-gradient(135deg,#3a3a3a,#8d7c6c 55%,#d9d4ce);position:relative}
.video-title{position:absolute;left:0;top:0;width:100%;height:28px;background:rgba(0,0,0,.75);color:#eee;font-size:10px;padding:8px 10px;white-space:nowrap;overflow:hidden}
.play{position:absolute;left:83px;top:65px;width:74px;height:48px;background:var(--orange);opacity:.9;display:flex;align-items:center;justify-content:center}
.market{left:93px;top:913px}
.product{top:943px;width:122px;height:150px;background:var(--card);border:1px solid var(--card-border)}
.product .img{position:absolute;left:9px;top:7px;width:104px;height:98px}
.product p{position:absolute;left:9px;top:111px;width:106px;font-size:9.3px;line-height:11px;color:#222}
.product .price{position:absolute;right:8px;top:134px;color:var(--orange);font-weight:700;font-size:10.5px}
.join-title{left:657px;top:913px}
.join-text{left:657px;top:942px;width:227px;font-size:9.3px;line-height:15px;text-align:justify}
.join{left:658px;top:1047px;width:154px;height:40px;border-radius:20px;background:linear-gradient(#f7a03a,var(--orange));border:1px solid #d95a10;color:#fff;font-family:Gelasio,Georgia,serif;font-weight:700;font-size:21px;display:flex;align-items:center;justify-content:center}
.copy{left:95px;top:1148px;font-size:9.5px;line-height:16px;color:#444}
.legal{right:84px;top:1148px;font-size:9.5px;color:#444}
.cards{right:84px;top:1167px;display:flex;gap:3px}
.cards span{width:29px;height:19px;border:1px solid #ccc;border-radius:2px;background:#f3f3f3}
</style>
</head>
<body>

<div class="abs brand">
  <div class="brand-name"><i></i>Lantern of Seers</div>
  <div class="brand-tag">a world of psychics</div>
</div>
<div class="abs util">Help<span>|</span>Login<span>|</span>Signup</div>

<nav class="abs nav">
  <a style="width:111px">Home Psychic</a><a style="width:106px">Marketplace</a><a style="width:118px">Psychic Profile</a><a style="width:117px">Psychic Store</a><a style="width:127px">Psychic product</a><a style="flex:1">Contact Us</a>
</nav>

<section class="abs hero"></section>
<div class="abs faces">
  <div class="face" role="img" aria-label="Portrait of a psychic reader"></div>
  <div class="face" role="img" aria-label="Portrait of a psychic reader"></div>
  <div class="face" role="img" aria-label="Portrait of a psychic reader"></div>
  <div class="face" role="img" aria-label="Portrait of a psychic reader"></div>
  <div class="face" role="img" aria-label="Portrait of a psychic reader"></div>
  <div class="face" role="img" aria-label="Portrait of a psychic reader"></div>
  <div class="face" role="img" aria-label="Portrait of a psychic reader"></div>
  <div class="face" role="img" aria-label="Portrait of a psychic reader"></div>
  <div class="face" role="img" aria-label="Portrait of a psychic reader"></div>
  <div class="face" role="img" aria-label="Portrait of a psychic reader"></div>
  <div class="face" role="img" aria-label="Portrait of a psychic reader"></div>
  <div class="face" role="img" aria-label="Portrait of a psychic reader"></div>
</div>
<div class="abs pill">Meet our Expert Lantern Seers</div>

<h2 class="abs best">The Best Psychics</h2>
<div class="abs best-text">
  <p>A live psychic reading is your chance to ask questions, get answer, simply dummy text of the printing and typesetting industry. Lorem Ipsum has been the industry's standard dummy text ever since.</p>
  <p>Ipsum has been the dummy text ever since Ipsum industry's standard dummy the 1500s,</p>
</div>

<h2 class="abs top-title">Top Pyschics</h2>

<svg width="0" height="0" style="position:absolute">
  <defs>
    <symbol id="star" viewBox="0 0 10 10"><path d="M5 .8l1.2 2.7 2.9.3-2.2 1.9.7 2.9L5 7.1 2.4 8.6l.7-2.9L.9 3.8l2.9-.3z" fill="#fff"/></symbol>
    <symbol id="chat" viewBox="0 0 20 18"><ellipse cx="8" cy="7" rx="7.5" ry="6" fill="#222"/><path d="M3 11l-1 5 5-3z" fill="#222"/><ellipse cx="14" cy="12" rx="5" ry="4" fill="#222" stroke="#ebebeb" stroke-width="1.2"/></symbol>
    <symbol id="mail" viewBox="0 0 20 14"><rect width="20" height="14" fill="#222"/><path d="M2 2l8 6 8-6M2 12l6-5M18 12l-6-5" stroke="#fff" stroke-width="1.2" fill="none"/></symbol>
    <symbol id="silhouette" viewBox="0 0 114 114"><path d="M42 20c0-12 30-14 32 2 2 8 0 20-6 26 10 6 24 8 30 14v52H16V62c6-6 20-8 30-14-5-6-5-18-4-28z" fill="#fff"/></symbol>
  </defs>
</svg>

<div class="abs card plain" style="left:92px">
  <div class="photo pic" role="img" aria-label="Portrait photo of psychic Mirela"><div class="nametag"><span class="dot on"></span>Mirela</div></div>
  <div class="stars"><b><svg width="9" height="9"><use href="#star"/></svg></b><b><svg width="9" height="9"><use href="#star"/></svg></b><b><svg width="9" height="9"><use href="#star"/></svg></b><b><svg width="9" height="9"><use href="#star"/></svg></b><b class="off"><svg width="9" height="9"><use href="#star"/></svg></b></div>
  <div class="rate r1"><svg width="18" height="16"><use href="#chat"/></svg>$ 12.00 / min</div>
  <div class="rate r2"><svg width="17" height="12"><use href="#mail"/></svg>$ 8.00 / Email</div>
</div>

<div class="abs card" style="left:252px">
  <div class="photo pic2" role="img" aria-label="Photo of psychic duo lumi and tara outdoors"><div class="nametag"><span class="dot on"></span>lumi &amp; tara</div></div>
  <div class="stars"><b><svg width="9" height="9"><use href="#star"/></svg></b><b><svg width="9" height="9"><use href="#star"/></svg></b><b><svg width="9" height="9"><use href="#star"/></svg></b><b><svg width="9" height="9"><use href="#star"/></svg></b><b class="off"><svg width="9" height="9"><use href="#star"/></svg></b></div>
  <div class="rate r1"><svg width="18" height="16"><use href="#chat"/></svg>$ 12.00 / min</div>
  <div class="rate r2"><svg width="17" height="12"><use href="#mail"/></svg>$ 8.00 / Email</div>
</div>

<div class="abs card" style="left:417px">
  <div class="photo avatar"><svg width="114" height="114"><use href="#silhouette"/></svg><div class="nametag"><span class="dot"></span>Arven</div></div>
  <div class="stars"><b><svg width="9" height="9"><use href="#star"/></svg></b><b><svg width="9" height="9"><use href="#star"/></svg></b><b><svg width="9" height="9"><use href="#star"/></svg></b><b><svg width="9" height="9"><use href="#star"/></svg></b><b class="off"><svg width="9" height="9"><use href="#star"/></svg></b></div>
  <div class="rate r1"><svg width="18" height="16"><use href="#chat"/></svg>$ 12.00 / min</div>
  <div class="rate r2"><svg width="17" height="12"><use href="#mail"/></svg>$ 8.00 / Email</div>
</div>

<div class="abs card" style="left:583px">
  <div class="photo avatar"><svg width="114" height="114"><use href="#silhouette"/></svg><div class="nametag"><span class="dot"></span>Oskar</div></div>
  <div class="stars"><b><svg width="9" height="9"><use href="#star"/></svg></b><b><svg width="9" height="9"><use href="#star"/></svg></b><b><svg width="9" height="9"><use href="#star"/></svg></b><b><svg width="9" height="9"><use href="#star"/></svg></b><b class="off"><svg width="9" height="9"><use href="#star"/></svg></b></div>
  <div class="rate r1"><svg width="18" height="16"><use href="#chat"/></svg>$ 12.00 / min</div>
  <div class="rate r2"><svg width="17" height="12"><use href="#mail"/></svg>$ 8.00 / Email</div>
</div>

<div class="abs card" style="left:747px">
  <div class="photo avatar"><svg width="114" height="114"><use href="#silhouette"/></svg><div class="nametag"><span class="dot"></span>Teo</div></div>
  <div class="stars"><b><svg width="9" height="9"><use href="#star"/></svg></b><b><svg width="9" height="9"><use href="#star"/></svg></b><b><svg width="9" height="9"><use href="#star"/></svg></b><b><svg width="9" height="9"><use href="#star"/></svg></b><b class="off"><svg width="9" height="9"><use href="#star"/></svg></b></div>
  <div class="rate r1"><svg width="18" height="16"><use href="#chat"/></svg>$ 12.00 / min</div>
  <div class="rate r2"><svg width="17" height="12"><use href="#mail"/></svg>$ 8.00 / Email</div>
</div>

<div class="abs viewmore">view more &raquo;</div>
<div class="abs rule" style="top:653px;width:792px"></div>

<h2 class="abs about">About Lantern of Seers.</h2>
<div class="abs about-text">
  <p>If you have an issue in your life that is causing you any sort of distress, no matter what it is, a reading from one of our psychics will give you immediate, compassionate insight. There are moments when you need more answers than you can get on your own. That's why the gifted psychics at Lantern of Seers are here for you, 24/7.</p>
  <p>Maybe your relationship suddenly fell apart and you don't know why. Perhaps you just lost a loved one and want to contact them. Maybe you suffered an unexpected financial crisis and you need to make a critical decision.</p>
  <p>All of our psychics are vetted before they come on board, so you don't have to spend critical time searching for someone you can trust. Many are born psychics, or developed their gifts at an early age, and come from back-grounds where these gifts run in their families. They all have many tools and abilities and they all love using their gifts to help people.</p>
</div>

<div class="abs video">
  <div class="video-inner" role="img" aria-label="Video still of a psychic speaking to camera">
    <div class="video-title">How to be psychic, have intuition, and do mind reading</div>
    <div class="play"><svg width="26" height="30"><path d="M2 2l22 13L2 28z" fill="#fff"/></svg></div>
  </div>
</div>

<div class="abs rule" style="top:892px;width:793px"></div>

<h2 class="abs market">Psychic Marketplace</h2>
<div class="abs product" style="left:92px">
  <div class="img" role="img" aria-label="Product photo of a patterned skirt" style="background:linear-gradient(#ddd,#6a4a4a)"></div>
  <p>All of our psychics are vetted.</p><span class="price">$75.00 USD</span>
</div>
<div class="abs product" style="left:232px">
  <div class="img" role="img" aria-label="Product photo of a goldfish bowl" style="background:linear-gradient(#eef4f6,#a8c8d6)"></div>
  <p>All of our psychics are vetted.</p><span class="price">$15.00 USD</span>
</div>
<div class="abs product" style="left:370px">
  <div class="img" role="img" aria-label="Product photo of shop shelves with bottles" style="background:linear-gradient(90deg,#c9b89c,#6f8a3e)"></div>
  <p>All of our psychics are vetted.</p><span class="price">$15.00 USD</span>
</div>
<div class="abs product" style="left:511px">
  <div class="img" role="img" aria-label="Product photo of a lit candle with ornaments" style="background:radial-gradient(circle at 50% 40%,#f3e9d6,#1a1a2a 60%)"></div>
  <p>All of our psychics are vetted.</p><span class="price">$15.00 USD</span>
</div>

<h2 class="abs join-title">Are you PSYCHIC?</h2>
<div class="abs join-text">All of our psychics are vetted before they come on board, so you don't have to spend critical time searching for someone you can trust. Many are born psychics, or developed their gifts at an early age, and come from backgrounds where these gifts run in their families.</div>
<div class="abs join">Join Now</div>

<div class="abs rule" style="top:1134px;left:88px;width:797px"></div>
<div class="abs copy">Copyright 2013 Lantern of Seers (ACN 000 111 222)<br>Trademark Lantern of Seers</div>
<div class="abs legal">Privacy Policy | Terms &amp; Conditions</div>
<div class="abs cards"><span></span><span></span><span></span><span></span><span></span></div>

</body>
</html>
```